Marlo's Bakes Tortehouse LLC website

Artisan cheesecake business looking for excellent talent to design bright, fun, engaging website for our company. We also recently acquired a food truck so we are able to cater and attend food truck events.
Our mission is to create fun, unique, delicious flavors of cheesecake and we bake them in mason jars and whole cheesecakes. We strive to exceed our customers' expectations in everything we do.
Target Market(s)
Foodies, cheesecake lovers, dessert lovers, food truck people,
Industry/Entity Type
Dessert, Catering, Pop Up events, Food truck
Coding
Coded - Design and coding required
Number of Pages Required
4 page
Requirements
Must have
- Pictures of my cheesecakes
Nice to have
- Bright, colorful, eye-catching design with a good flow

```html
<!DOCTYPE html>
<html lang="en">
<head>
<meta charset="utf-8">
<title>Marlo's Bakes Tortehouse LLC</title>
<link rel="stylesheet" href="https://fonts.googleapis.com/css2?family=Poppins:wght@400;500;600&family=Yesteryear&family=Yellowtail&display=block">
<style>
:root{
  --pink:#e2449a;
  --pink-deep:#d6317f;
  --pink-hero:#e86aa8;
  --blush:#fde6f0;
  --blush-2:#fbd5e6;
  --ink:#222;
  --muted:#555;
  --white:#fff;
  --script:'Yesteryear','Yellowtail',cursive;
}
*{box-sizing:border-box;margin:0;padding:0}
html,body{width:1200px;height:4728px;overflow:hidden}
body{position:relative;background:var(--blush);font-family:'Poppins',sans-serif;color:var(--ink)}
.abs{position:absolute}
.script{font-family:var(--script);color:var(--pink);font-weight:400}
.ph{border-radius:14px}

/* top */
.notice{left:0;top:0;width:1200px;height:30px;background:var(--blush);text-align:center;font-size:10px;line-height:30px;color:var(--pink);text-decoration:underline;font-weight:500}
.nav{left:0;top:30px;width:1200px;height:56px;background:#fbe9f1}
.logo{left:133px;top:33px;width:100px;height:100px;border-radius:50%;background:var(--pink-hero);border:5px solid var(--white);display:flex;align-items:center;justify-content:center;text-align:center;z-index:3}
.logo span{color:var(--white);font-size:13px;font-weight:500;line-height:16px}
.menu{left:413px;top:30px;height:56px;display:flex;align-items:center;gap:24px;font-size:10px;font-weight:600}
.nav-icons{left:966px;top:30px;height:56px;display:flex;align-items:center;gap:16px;color:var(--ink);font-size:10px}

/* hero */
.hero{left:0;top:86px;width:1200px;height:560px}
.hero-card{top:189px;width:389px;height:490px;background:var(--white);border-radius:26px;padding:9px}
.hero-card .ph{width:100%;height:100%;border-radius:20px}
.hero-label{left:215px;top:470px;width:358px;height:190px;background:rgba(255,255,255,.85);border-radius:18px;padding:18px 22px}
.hero-label h1{font-size:48px;line-height:52px;color:var(--pink);font-weight:500}
.hero-label a{position:absolute;left:38px;top:144px;font-size:10px;color:var(--pink);text-decoration:underline}

/* welcome */
.welcome-kicker{left:132px;top:774px;font-size:24px;white-space:nowrap}
.welcome-title{left:126px;top:806px;font-size:44px;line-height:54px;white-space:nowrap}
.welcome-copy{left:602px;top:737px;width:466px;font-size:11px;line-height:21.8px;color:var(--muted);text-align:justify}
.btn{left:602px;top:925px;width:117px;height:34px;border-radius:17px;background:var(--pink);color:var(--white);font-size:10.5px;font-weight:600;line-height:34px;text-align:center}
.rule{left:132px;width:936px;height:1px;background:#e9a8c6}

.section-title{font-size:46px;white-space:nowrap;line-height:60px}
.center{left:0;width:1200px;text-align:center}

/* cards */
.card{width:272px;height:349px;background:var(--white);border-radius:16px;padding:8px}
.card .ph{height:224px;border-radius:12px}
.card h3{font-family:var(--script);color:var(--pink);font-weight:400;font-size:25px;line-height:30px;margin:10px 0 4px 10px;white-space:nowrap}
.card p{font-size:10.5px;line-height:19px;color:var(--muted);margin-left:10px;white-space:nowrap}
.price{margin:3px 0 0 10px;font-size:15px;font-weight:600}
.price em{font-family:var(--script);color:var(--pink);font-style:normal;font-weight:400;font-size:13px;margin-right:6px}

/* calendar */
.calendar{left:182px;top:1756px;width:427px;height:396px;background:var(--white);border-radius:6px;box-shadow:0 2px 8px rgba(0,0,0,.08)}
.cal-month{position:absolute;left:57px;top:32px;font-size:15px}
.cal-nav{position:absolute;right:50px;top:30px;color:#999;font-size:18px;letter-spacing:18px}
.cal-grid{position:absolute;left:32px;top:90px;display:grid;grid-template-columns:repeat(7,51.4px);grid-auto-rows:51.4px}
.cal-grid div{display:flex;align-items:center;justify-content:center;font-size:14px}
.cal-grid .dow{font-size:12px;font-weight:500;height:20px}
.cal-grid .past span{width:32px;height:32px;border-radius:8px;background:#f4f4f4;color:#aaa;display:flex;align-items:center;justify-content:center;font-size:13px}
.cal-grid .today span{width:34px;height:34px;border-radius:8px;background:var(--pink);color:var(--white);display:flex;align-items:center;justify-content:center}
.cal-grid .next{color:#aaa}
.event{left:629px;width:388px;height:120px;background:var(--white);border-radius:4px;box-shadow:0 2px 8px rgba(0,0,0,.08)}
.event .ph{position:absolute;left:6px;top:6px;width:123px;height:108px;border-radius:2px}
.event-body{position:absolute;left:141px;top:16px;width:240px}
.event-date{font-size:9px;color:var(--pink);font-weight:600}
.event-title{font-family:var(--script);font-size:19px;line-height:22px;margin:4px 0 3px;color:var(--ink)}
.event-note{font-size:10.5px}

/* how it works */
.step{top:2967px;width:224px;height:290px;background:var(--white);border-radius:16px;text-align:center;padding-top:24px}
.step.active{background:var(--pink);color:var(--white)}
.step h3{font-family:var(--script);font-weight:400;font-size:25px;color:var(--pink);margin-top:8px}
.step.active h3{color:var(--white)}
.step hr{width:40px;border:0;border-top:2px solid currentColor;margin:8px auto 14px}
.step p{font-size:10.5px;line-height:21px;padding:0 22px}

/* testimonial */
.testimonials{left:0;top:3345px;width:1200px;height:435px;background:var(--blush-2)}
.quote{left:268px;top:3492px;width:664px;height:224px;background:var(--white);border-radius:22px;text-align:center;padding:30px 58px;font-size:15.5px;line-height:32px;font-style:italic;color:#333;box-shadow:0 3px 10px rgba(0,0,0,.1)}
.quote .who{font-family:var(--script);font-style:normal;color:var(--pink);font-size:21px}

.insta{width:178px}

/* footer */
.footer{left:0;top:4200px;width:1200px;height:528px}
.foot-logo{left:178px;top:4419px;width:202px;height:202px;border-radius:50%;background:var(--white);border:5px solid var(--pink);box-shadow:0 0 0 6px var(--white);display:flex;flex-direction:column;align-items:center;justify-content:center;color:var(--pink)}
.foot-logo strong{font-size:26px;font-weight:500}
.foot-logo small{font-size:10px;margin-top:2px}
.foot-col{top:4405px;color:var(--white);font-size:12px}
.foot-col h4{font-family:var(--script);font-weight:400;font-size:23px;margin-bottom:12px}
.foot-col li{list-style:none;line-height:22px;display:flex;align-items:center;gap:10px}
.foot-col li i{font-style:normal;width:14px;display:inline-flex;justify-content:center}
.dot{width:10px;height:10px;border-radius:50%;background:var(--white);display:inline-block}
.pay{top:4598px;width:38px;height:24px;background:var(--white);border-radius:3px}
.foot-line{left:66px;top:4667px;width:1068px;height:1px;background:rgba(255,255,255,.6)}
.copy{left:0;top:4684px;width:1200px;text-align:center;color:var(--white);font-size:10px}
.copy b{font-family:var(--script);font-weight:400;font-size:15px}
</style>
</head>
<body>

<div class="abs notice">LEARN MORE ABOUT OUR COVID-19 RESPONSE AND HOW WE'RE KEEPING YOU SAFE. &nbsp;⟶</div>
<div class="abs nav"></div>
<div class="abs logo"><span>Marlo's<br>Bakes</span></div>
<nav class="abs menu"><span>HOME</span><span>ABOUT US</span><span>PRODUCTS</span><span>ORDERING PROCESS</span><span>MENU</span><span>EVENTS</span><span>CONTACT US</span></nav>
<div class="abs nav-icons">
  <svg width="12" height="12" viewBox="0 0 12 12"><rect x="2" y="4" width="8" height="7" rx="1" fill="#222"/><path d="M4 4V3a2 2 0 0 1 4 0v1" stroke="#222" fill="none"/></svg>|
  <svg width="12" height="12" viewBox="0 0 12 12"><circle cx="5" cy="5" r="3.5" stroke="#222" stroke-width="1.6" fill="none"/><path d="M7.5 7.5L11 11" stroke="#222" stroke-width="1.6"/></svg>|
  <svg width="12" height="12" viewBox="0 0 12 12"><circle cx="6" cy="3.5" r="2.5" fill="#222"/><path d="M1 11a5 4 0 0 1 10 0z" fill="#222"/></svg>
</div>

<!-- hero -->
<svg class="abs hero" width="1200" height="560" viewBox="0 0 1200 560" role="img" aria-label="Blurred pink close-up of whipped cheesecake slices">
  <defs><linearGradient id="heroFill" x1="0" y1="0" x2="1" y2="1"><stop offset="0" stop-color="#e98abb"/><stop offset=".5" stop-color="#e56aa6"/><stop offset="1" stop-color="#df5d9c"/></linearGradient></defs>
  <path d="M0 0H1200V540C1000 470 860 440 600 440C380 440 200 470 0 540Z" fill="url(#heroFill)"/>
  <path d="M0 545C200 475 380 446 600 446C860 446 1000 476 1200 545" stroke="#d6317f" stroke-width="7" fill="none"/>
</svg>
<div class="abs hero-card" style="left:198px"><div class="ph" role="img" aria-label="Cheesecake topped with whipped cream and cocoa" style="background:linear-gradient(180deg,#4f6b35 0%,#8a6a4a 40%,#e8ddd0 70%,#7a5336 100%)"></div></div>
<div class="abs hero-card" style="left:611px"><div class="ph" role="img" aria-label="Mason jar cheesecakes beside a cookie package" style="background:linear-gradient(180deg,#2a4f9a 0%,#3a5fa8 30%,#c9b9a4 55%,#b08a5e 100%)"></div></div>
<div class="abs hero-label"><h1>Flavored<br>Cakes</h1><a>LEARN MORE</a>
  <svg class="abs" style="left:222px;top:146px" width="64" height="8"><path d="M0 4H62M57 1L62 4L57 7" stroke="#e2449a" fill="none"/></svg></div>

<!-- welcome -->
<div class="abs welcome-kicker">Welcome to Marlo's Bakes</div>
<div class="abs script welcome-title">Lorem ipsum dolor sit amet<br>consectetur adipisc.</div>
<svg class="abs" style="left:132px;top:920px" width="54" height="14"><path d="M0 7H52M45 1L52 7L45 13" stroke="#e2449a" stroke-width="1.5" fill="none"/></svg>
<p class="abs welcome-copy">Lorem ipsum dolor sit amet, consectetur adipiscing elit, sed do eiusmod tempor incididunt ut labore et dolore magna aliqua. Quis ipsum suspendisse ultrices gravida. Risus commodo viverra maecenas accumsan lacus vel facilisis. Iste natus error sit voluptatem accusantium doloremque laudantium, totam rem aperiam, eaque ipsa quae ab illo inventore veritatis et quasi architecto beatae vitae dicta sunt explicabo. Nemo enim ipsam voluptatem quia voluptas sit aspernatur aut odit aut fugit, sed quia consequuntur magni dolores eos qui ratione sequi nesciunt. Neque porro quisquam est.</p>
<div class="abs btn">LEARN MORE</div>
<div class="abs rule" style="top:1028px"></div>

<!-- products -->
<div class="abs script section-title" style="left:128px;top:1080px">Our Products</div>
<svg class="abs" style="left:954px;top:1102px" width="120" height="16"><path d="M2 8H52M9 2L2 8L9 14" stroke="#e9a8c6" stroke-width="1.5" fill="none"/><path d="M68 8H118M111 2L118 8L111 14" stroke="#e2449a" stroke-width="1.5" fill="none"/></svg>
<div class="abs card" style="left:132px;top:1165px"><div class="ph" role="img" aria-label="Slice of chocolate cheesecake with chocolate shavings" style="background:linear-gradient(180deg,#6b4a35,#9b7a62 60%,#eee 100%)"></div><h3>Lorem ipsum dolor sit amet</h3><p>Lorem ipsum dolor sit amet, consectetur<br>adipiscing elit sed do eiusmod.</p><div class="price"><em>Price:</em>£ 120:00</div></div>
<div class="abs card" style="left:424px;top:1165px"><div class="ph" role="img" aria-label="Slice of cookies and cream cheesecake" style="background:linear-gradient(180deg,#ddd,#e8e2da 55%,#3a3432 100%)"></div><h3>Lorem ipsum dolor sit amet</h3><p>Lorem ipsum dolor sit amet, consectetur<br>adipiscing elit sed do eiusmod.</p><div class="price"><em>Price:</em>£ 120:00</div></div>
<div class="abs card" style="left:717px;top:1165px"><div class="ph" role="img" aria-label="Slice of cheesecake with teal drizzle and brownie chunks" style="background:linear-gradient(180deg,#2e8f8f,#4b3026 45%,#7ed7d5 80%,#3b2a22 100%)"></div><h3>Lorem ipsum dolor sit amet</h3><p>Lorem ipsum dolor sit amet, consectetur<br>adipiscing elit sed do eiusmod.</p><div class="price"><em>Price:</em>£ 120:00</div></div>
<div class="abs card" style="left:1011px;top:1165px"><div class="ph" role="img" aria-label="Strawberry cheesecake slice with fresh strawberries" style="background:linear-gradient(180deg,#e27a84,#f3e7d2 60%,#c4242e 100%)"></div><h3>Lorem ipsum dolor sit amet</h3><p>Lorem ipsum dolor sit amet, consectetur<br>adipiscing elit sed do eiusmod.</p><div class="price"><em>Price:</em>£ 120:00</div></div>
<div class="abs rule" style="top:1600px"></div>

<!-- events -->
<div class="abs script section-title center" style="top:1665px">Calendar of Monthly Events</div>
<div class="abs calendar">
  <div class="cal-month">May 2022</div>
  <div class="cal-nav">‹›</div>
  <div class="cal-grid">
    <div class="dow">Su</div><div class="dow">Mo</div><div class="dow">Tu</div><div class="dow">We</div><div class="dow">Th</div><div class="dow">Fr</div><div class="dow">Sa</div>
    <div class="past"><span>27</span></div><div class="past"><span>28</span></div><div class="past"><span>1</span></div><div class="past"><span>2</span></div><div class="past"><span>3</span></div><div class="past"><span>4</span></div><div class="past"><span>5</span></div>
    <div class="past"><span>6</span></div><div class="past"><span>7</span></div><div class="past"><span>8</span></div><div class="past"><span>9</span></div><div class="past"><span>10</span></div><div class="past"><span>11</span></div><div class="past"><span>12</span></div>
    <div class="past"><span>13</span></div><div class="today"><span>14</span></div><div>15</div><div>16</div><div>17</div><div>18</div><div>19</div>
    <div>20</div><div>21</div><div>22</div><div>23</div><div>24</div><div>25</div><div>26</div>
    <div>27</div><div>28</div><div>29</div><div>30</div><div>31</div><div class="next">1</div><div class="next">2</div>
  </div>
</div>
<div class="abs event" style="top:1756px"><div class="ph" role="img" aria-label="Guests posing at a food truck event" style="background:linear-gradient(135deg,#6f6a70,#c7b8b0 60%,#3a3a3a)"></div><div class="event-body"><div class="event-date">30 JUNE 2022</div><div class="event-title">Lorem ipsum dolor sit amet cons ectetur sed do eiusmod.</div><div class="event-note">Lorem ipsum dolor sit amet consectetur.</div></div></div>
<div class="abs event" style="top:1896px"><div class="ph" role="img" aria-label="Team members standing outdoors at an event" style="background:linear-gradient(135deg,#7aa3d6,#e7b9cc 55%,#2f2f2f)"></div><div class="event-body"><div class="event-date">30 JUNE 2022</div><div class="event-title">Lorem ipsum dolor sit amet cons ectetur sed do eiusmod.</div><div class="event-note">Lorem ipsum dolor sit amet consectetur.</div></div></div>
<div class="abs event" style="top:2035px"><div class="ph" role="img" aria-label="Event schedule flyer" style="background:linear-gradient(135deg,#1f1f1f,#f07fb2 50%,#f3d9e6)"></div><div class="event-body"><div class="event-date">30 JUNE 2022</div><div class="event-title">Lorem ipsum dolor sit amet cons ectetur sed do eiusmod.</div><div class="event-note">Lorem ipsum dolor sit amet consectetur.</div></div></div>
<div class="abs rule" style="top:2239px"></div>

<!-- menu -->
<div class="abs script section-title" style="left:128px;top:2291px">Our Menu</div>
<svg class="abs" style="left:954px;top:2313px" width="120" height="16"><path d="M2 8H52M9 2L2 8L9 14" stroke="#e9a8c6" stroke-width="1.5" fill="none"/><path d="M68 8H118M111 2L118 8L111 14" stroke="#e2449a" stroke-width="1.5" fill="none"/></svg>
<div class="abs card" style="left:132px;top:2376px"><div class="ph" role="img" aria-label="Whole cheesecake topped with cookies and chocolate drip" style="background:linear-gradient(180deg,#c9a57a,#5a3524 55%,#2b1a12)"></div><h3>Lorem ipsum dolor sit amet</h3><p>Lorem ipsum dolor sit amet, consectetur<br>adipiscing elit sed do eiusmod.</p><div class="price"><em>Price:</em>£ 120:00</div></div>
<div class="abs card" style="left:424px;top:2376px"><div class="ph" role="img" aria-label="Whole cheesecake with cookie dough and teal drip" style="background:linear-gradient(180deg,#d8c4a6,#3a2a22 45%,#5ec9c7 80%,#f2f2f2)"></div><h3>Lorem ipsum dolor sit amet</h3><p>Lorem ipsum dolor sit amet, consectetur<br>adipiscing elit sed do eiusmod.</p><div class="price"><em>Price:</em>£ 120:00</div></div>
<div class="abs card" style="left:717px;top:2376px"><div class="ph" role="img" aria-label="Chocolate drip cheesecake with cream rosettes" style="background:linear-gradient(180deg,#d9d3cc,#5b3a27 45%,#e9d6b9 85%)"></div><h3>Lorem ipsum dolor sit amet</h3><p>Lorem ipsum dolor sit amet, consectetur<br>adipiscing elit sed do eiusmod.</p><div class="price"><em>Price:</em>£ 120:00</div></div>
<div class="abs card" style="left:1011px;top:2376px"><div class="ph" role="img" aria-label="Chocolate cheesecake with marshmallow topping" style="background:linear-gradient(180deg,#e6e1dc,#6a3f2a 50%,#3d241a)"></div><h3>Lorem ipsum dolor sit amet</h3><p>Lorem ipsum dolor sit amet, consectetur<br>adipiscing elit sed do eiusmod.</p><div class="price"><em>Price:</em>£ 120:00</div></div>
<div class="abs rule" style="top:2820px"></div>

<!-- how it works -->
<div class="abs script section-title center" style="top:2873px">How It Works</div>
<svg width="0" height="0" style="position:absolute"><defs><symbol id="cake" viewBox="0 0 48 48"><path d="M14 10v6M24 8v8M34 10v6" stroke="currentColor" stroke-width="2"/><circle cx="14" cy="8" r="1.6" fill="currentColor"/><circle cx="24" cy="6" r="1.6" fill="currentColor"/><circle cx="34" cy="8" r="1.6" fill="currentColor"/><rect x="10" y="16" width="28" height="9" rx="1" stroke="currentColor" stroke-width="2" fill="none"/><rect x="6" y="25" width="36" height="11" rx="1" stroke="currentColor" stroke-width="2" fill="none"/><path d="M3 40H45" stroke="currentColor" stroke-width="2"/><path d="M6 29c4 3 6 3 9 0s6 3 9 0 6 3 9 0 6 3 9 0" stroke="currentColor" stroke-width="1.5" fill="none"/></symbol></defs></svg>
<div class="abs step" style="left:132px;color:var(--pink)"><svg width="48" height="48"><use href="#cake"/></svg><h3>Lorem ipsum dolor</h3><hr><p style="color:var(--ink)">Lorem ipsum dolor sit amet, consectetur adipiscing elit, sed do eiusmod tempor incididunt ut labore et dolore magna aliqua Quis ipsum suspendisse ultrices gravida Risus commodo viverra.</p></div>
<div class="abs step active" style="left:369px"><svg width="48" height="48"><use href="#cake"/></svg><h3>Lorem ipsum dolor</h3><hr><p>Lorem ipsum dolor sit amet, consectetur adipiscing elit, sed do eiusmod tempor incididunt ut labore et dolore magna aliqua Quis ipsum suspendisse ultrices gravida Risus commodo viverra.</p></div>
<div class="abs step" style="left:607px;color:var(--pink)"><svg width="48" height="48"><use href="#cake"/></svg><h3>Lorem ipsum dolor</h3><hr><p style="color:var(--ink)">Lorem ipsum dolor sit amet, consectetur adipiscing elit, sed do eiusmod tempor incididunt ut labore et dolore magna aliqua Quis ipsum suspendisse ultrices gravida Risus commodo viverra.</p></div>
<div class="abs step" style="left:844px;color:var(--pink)"><svg width="48" height="48"><use href="#cake"/></svg><h3>Lorem ipsum dolor</h3><hr><p style="color:var(--ink)">Lorem ipsum dolor sit amet, consectetur adipiscing elit, sed do eiusmod tempor incididunt ut labore et dolore magna aliqua Quis ipsum suspendisse ultrices gravida Risus commodo viverra.</p></div>

<!-- testimonials -->
<div class="abs testimonials"></div>
<div class="abs script section-title center" style="top:3404px">Our Client Testimonials</div>
<div class="abs quote">our goal is to exceed Customers'expectations and we love seeing the smiles that our cheesecakes bring to everyone! Cheesecake is a love like no other. It's unique,beautiful, and mysterious. We put our art is an spin on it resulting in exquisite flavors that are unforgettable.<br><span class="who">- Jenna Price</span></div>

<!-- follow -->
<div class="abs script section-title center" style="top:3840px">Follow us @yourtortedealer</div>
<div class="abs insta ph" style="left:132px;top:3930px;height:185px;background:linear-gradient(135deg,#f2b6cf,#e27fae 60%,#7a6a6a)" role="img" aria-label="Pink food truck with owner in front"></div>
<div class="abs insta ph" style="left:321px;top:3975px;height:181px;background:linear-gradient(180deg,#f4ecec,#d84a5a 55%,#f3e2dc)" role="img" aria-label="Strawberry cheesecake jars"></div>
<div class="abs insta ph" style="left:510px;top:3930px;height:185px;background:linear-gradient(135deg,#e8d9c4,#7a4a2a 50%,#c89a5a)" role="img" aria-label="Chocolate cheesecake with caramel lattice"></div>
<div class="abs insta ph" style="left:701px;top:3975px;height:181px;background:linear-gradient(180deg,#e9e6e2,#f1c23b 50%,#d8962a)" role="img" aria-label="Lemon bundt cheesecake"></div>
<div class="abs insta ph" style="left:890px;top:3930px;height:185px;background:linear-gradient(135deg,#9ec66b,#e6f0d4 55%,#6aa33d)" role="img" aria-label="Key lime cheesecake with lime slices"></div>

<!-- footer -->
<svg class="abs footer" width="1200" height="528" viewBox="0 0 1200 528">
  <path d="M0 40C200 110 380 140 600 140C820 140 1000 100 1200 20V528H0Z" fill="#e2449a"/>
  <path d="M0 58C200 128 380 158 600 158C820 158 1000 118 1200 38" stroke="#fff" stroke-width="4" fill="none"/>
</svg>
<div class="abs foot-logo"><strong>Marlo's Bakes</strong><small>ARTISAN CHEESECAKES</small></div>
<div class="abs foot-col" style="left:473px"><h4>Quick Links</h4><ul>
  <li><i>»</i>Home</li><li><i>»</i>About Us</li><li><i>»</i>Products</li><li><i>»</i>Ordering Process</li><li><i>»</i>Menu</li><li><i>»</i>Events</li><li><i>»</i>Contact Us</li></ul></div>
<div class="abs foot-col" style="left:664px"><h4>Follow Us</h4><ul>
  <li><i><span class="dot"></span></i>Faceboard</li><li><i><span class="dot"></span></i>Pictogram</li><li><i><span class="dot"></span></i>Chirper</li><li><i><span class="dot"></span></i>Linkwork</li><li><i><span class="dot"></span></i>Viewtube</li></ul></div>
<div class="abs foot-col" style="left:864px;width:230px"><h4>Contact Us</h4><ul>
  <li style="align-items:flex-start"><i><svg width="10" height="14" viewBox="0 0 10 14"><path d="M5 0a5 5 0 0 1 5 5c0 4-5 9-5 9S0 9 0 5a5 5 0 0 1 5-5z" fill="#fff"/><circle cx="5" cy="5" r="2" fill="#e2449a"/></svg></i>123 Lorem ipsum dolor sit amet consectetur adipiscing.</li>
  <li style="margin-top:6px"><i><svg width="12" height="12" viewBox="0 0 12 12"><path d="M2 1l2.5 0 1 3-1.5 1a7 7 0 0 0 3 3l1-1.5 3 1V11A9 9 0 0 1 1 2z" fill="#fff"/></svg></i>+1 305-555-0148</li>
  <li style="margin-top:12px"><i><svg width="12" height="9" viewBox="0 0 12 9"><rect width="12" height="9" rx="1" fill="#fff"/><path d="M0 1l6 4 6-4" stroke="#e2449a" fill="none"/></svg></i>hello@marlosbakes.example</li></ul></div>
<div class="abs pay" style="left:868px"></div>
<div class="abs pay" style="left:910px"></div>
<div class="abs pay" style="left:952px"></div>
<div class="abs pay" style="left:994px"></div>
<div class="abs foot-line"></div>
<div class="abs copy">© copyrights 2022 <b>Marlo's Bakes</b> &nbsp;| &nbsp;&nbsp;All rights reserved.</div>

</body>
</html>
```